Marlow Crest Group (Real Estate and Investment)

A high end, clean design.
We are a real estate company with sales, asset management and investment divisions. We want to use a black and white scheme which is really high end feel. The back of the card can just be the logo (black background with the white writing) as we will probably emboss this when we print)

Target Market(s)

High level investors, high end houses for sale

Industry/Entity Type

Business

Contact Information for Business Card

Name, position, phone number and email address
Glen Varley, Managing Director, 0437259064 and glen@marlowcrest-example.com.au

Requirements
Must have
• Back of the card to be the black background with the white writing (as per the attached images). Would like the capacity to emboss the writing and logo

```html
<!DOCTYPE html>
<html lang="en">
<head>
<meta charset="utf-8">
<title>Marlow Crest Group — Business Card</title>
<link href="https://fonts.googleapis.com/css2?family=Inter:wght@400;500&display=swap" rel="stylesheet">
<style>
  :root {
    --paper: #ffffff;
    --ink: #111111;
    --card-black: #000000;
    --card-white: #ffffff;
    --edge: #6e6e6e;
    --ghost: #e4e4e4;
  }
  * { margin: 0; padding: 0; box-sizing: border-box; }
  html, body {
    width: 1200px;
    height: 846px;
    overflow: hidden;
    background: var(--paper);
    font-family: "Inter", "Helvetica Neue", Arial, sans-serif;
  }
  .presentation {
    position: relative;
    width: 1200px;
    height: 846px;
    overflow: hidden;
  }
  .backdrop-ring {
    position: absolute;
    left: 0;
    top: 0;
    width: 1200px;
    height: 846px;
  }
  .card {
    position: absolute;
    left: 528px;
    width: 514px;
    height: 314px;
    border-radius: 13px;
    overflow: hidden;
  }
  .card--front {
    top: 67px;
    background: var(--card-white);
    border: 1px solid var(--edge);
    color: var(--ink);
  }
  .card--back {
    top: 465px;
    background: var(--card-black);
    color: var(--card-white);
  }
  .card__ring {
    position: absolute;
    left: 0;
    top: 0;
    width: 514px;
    height: 314px;
  }
  .brand-dot {
    position: absolute;
    left: 104px;
    top: 37px;
    width: 80px;
    height: 74px;
    border-radius: 50%;
    border: 1.5px solid currentColor;
  }
  .brand-name {
    position: absolute;
    left: 50px;
    top: 128px;
    font-size: 18px;
    font-weight: 500;
    letter-spacing: -0.2px;
    white-space: nowrap;
  }
  .holder {
    position: absolute;
    left: 50px;
    top: 196px;
    font-size: 12px;
    line-height: 15px;
  }
  .holder__name { padding-left: 9px; }
  .contact {
    position: absolute;
    left: 36px;
    top: 238px;
    list-style: none;
    font-size: 13.5px;
    line-height: 22px;
  }
  .contact li {
    display: flex;
    align-items: center;
    gap: 5px;
  }
  .contact svg { width: 10px; height: 12px; flex: none; }
</style>
</head>
<body>
<main class="presentation">

  <svg class="backdrop-ring" viewBox="0 0 1200 846" aria-hidden="true">
    <circle cx="205" cy="424" r="236" fill="none" stroke="var(--ghost)" stroke-width="10"/>
  </svg>

  <section class="card card--front" aria-label="Business card front">
    <svg class="card__ring" viewBox="0 0 514 314" aria-hidden="true">
      <circle cx="492" cy="312" r="196" fill="none" stroke="#000" stroke-width="6"/>
    </svg>
    <span class="brand-dot" aria-hidden="true"></span>
    <p class="brand-name">MARLOW CREST GROUP</p>
    <div class="holder">
      <p class="holder__name">Glen Varley</p>
      <p class="holder__role">Managing Director</p>
    </div>
    <ul class="contact">
      <li>
        <svg viewBox="0 0 10 12" aria-hidden="true">
          <rect x="2" y="0.5" width="6" height="11" rx="0.8" fill="none" stroke="#111" stroke-width="1.2"/>
          <rect x="3.2" y="2" width="3.6" height="3" fill="#111"/>
          <rect x="3.2" y="6.2" width="3.6" height="3.8" fill="#111"/>
        </svg>
        <span>0437 259 064</span>
      </li>
      <li>
        <svg viewBox="0 0 12 10" aria-hidden="true" style="width:12px;height:10px">
          <rect x="0.6" y="1.5" width="10.8" height="7" fill="none" stroke="#111" stroke-width="1.2"/>
          <path d="M0.6 1.5 L6 5.6 L11.4 1.5 M0.6 8.5 L4.5 4.5 M11.4 8.5 L7.5 4.5" fill="none" stroke="#111" stroke-width="1.1"/>
        </svg>
        <span>glen@marlowcrest-example.com.au</span>
      </li>
    </ul>
  </section>

  <section class="card card--back" aria-label="Business card back">
    <svg class="card__ring" viewBox="0 0 514 314" aria-hidden="true">
      <circle cx="492" cy="312" r="196" fill="none" stroke="#fff" stroke-width="6"/>
    </svg>
    <span class="brand-dot" aria-hidden="true"></span>
    <p class="brand-name">MARLOW CREST GROUP</p>
  </section>

</main>
</body>
</html>
```